Referral Card thats different from the rest

Business card size-

Referral card that will be given to clients, in turn they will pass it on to their friends.

The referee will add their name and address, and friends name to card before it is passed on

Referee gets 2 FREE movie tickets

Friend gets $25 OFF their service

Company is an electrical contracting company specialising in the domestic market.

I would like the card to be fun not so serious!
Completely open minded to any and every creative idea!

attached is 2 photo of an example of what another business has, i am trying to achieve something similiar
Updates

I have increased the budget, ;)

i have added 2 x photos of what i am trying to achieve. this is from another business, I am after something similar to this
Thanks

I have updated the design brief.
this should help make it easir and more clear
Thanks

Target Market(s)

Home owners from 30yrs +

Industry/Entity Type

Electrical

Requirements
Must have
• Logo - Not a main feature of card
1300 574 862 on both sides
Lic no: 381946D (doesn’t have to be big) prefer on back

The main feature of the front of the card is the 2 free movie tickets for Referee & $25 OFF Friends first bill

HOW ABOUT TWO FREE MOVIE TICKETS?
It is easy! Know someone who needs an electrician? Maybe a friend, family member, relative or work colleague.
Tell them about us, and we will take $25 off their first bill and give you two FREE Movie Tickets just for introducing us.
To make a referral fill out this card and give it to your friend.

Recommended By:____________
Address:__________________
Frinds name: _____________

*this offer is only valued for work over $55. Non transferable for cash. This coupon is limited to 1 per customer, not to be used in conjunction with any other offer
Nice to have
• Catchy heading on card
example- tell a friend for cash card, (if i was giving away cash vouchers..)

example- keep me in your wallet and pass me on

```html
<!DOCTYPE html>
<html lang="en">
<head>
<meta charset="utf-8">
<title>Referral Card – Tell a Friend</title>
<link rel="stylesheet" href="https://fonts.googleapis.com/css2?family=Anton&family=Open+Sans:wght@400;600;700&display=swap">
<style>
  :root {
    --stage: #d9d9d9;
    --paper: #f5f5f3;
    --ink: #141414;
    --band: #1b1b1b;
    --orange: #e0801f;
    --rule: #3a3a3a;
    --art-green: #4a8d3f;
    --art-skin: #e2c196;
    --art-blue: #a7c8e2;
    --art-red: #b8402f;
  }
  * { box-sizing: border-box; margin: 0; padding: 0; }
  html, body { width: 1200px; height: 900px; overflow: hidden; }
  body {
    background: var(--stage);
    font-family: "Open Sans", Arial, sans-serif;
    color: var(--ink);
    position: relative;
  }
  .card {
    position: absolute;
    top: 285px;
    width: 540px;
    height: 330px;
    background: var(--paper);
    overflow: hidden;
    box-shadow: 0 6px 18px rgba(0,0,0,.18);
  }
  .card--back { left: 40px; }
  .card--front { left: 620px; }
  .display { font-family: "Anton", Impact, sans-serif; text-transform: uppercase; letter-spacing: .5px; line-height: 1; }

  /* Back side */
  .back-band {
    position: absolute; top: 0; left: 0; right: 0; height: 52px;
    background: var(--band);
    display: flex; align-items: center; justify-content: center;
  }
  .back-band .display { color: var(--orange); font-size: 27px; }
  .details-heading {
    position: absolute; top: 70px; left: 0; right: 0; text-align: center;
    font-family: "Anton", Impact, sans-serif; font-size: 12px; letter-spacing: .5px;
  }
  .back-phone { position: absolute; top: 88px; left: 0; right: 0; text-align: center; font-size: 36px; }
  .referral-form { position: absolute; top: 150px; left: 38px; right: 38px; }
  .form-row {
    display: flex; align-items: flex-end; gap: 8px; height: 30px;
    font-size: 11px; text-transform: uppercase; letter-spacing: .3px;
  }
  .form-row .fill { flex: 1; border-bottom: 1px solid var(--rule); height: 1px; margin-bottom: 3px; }
  .fine-print {
    position: absolute; top: 258px; left: 50px; right: 50px; text-align: center;
    font-size: 9px; line-height: 1.4;
  }
  .licence { position: absolute; right: 20px; bottom: 12px; font-size: 10px; text-transform: uppercase; }

  /* Front side */
  .offer-left { position: absolute; top: 18px; left: 22px; }
  .offer-right { position: absolute; top: 18px; right: 22px; text-align: right; }
  .offer-big { color: var(--orange); font-size: 54px; }
  .offer-sub { font-size: 15px; margin-top: 4px; }
  .ampersand {
    position: absolute; top: 10px; left: 0; right: 0; text-align: center;
    font-family: "Anton", Impact, sans-serif; font-size: 78px; line-height: 1;
  }
  .pitch { position: absolute; top: 108px; left: 40px; right: 40px; text-align: center; }
  .pitch-heading { font-family: "Anton", Impact, sans-serif; font-size: 13px; letter-spacing: .5px; margin-bottom: 4px; }
  .pitch p { font-size: 9.5px; line-height: 1.45; }
  .front-phone { position: absolute; right: 26px; top: 196px; font-size: 46px; }
  .front-band {
    position: absolute; left: 0; right: 0; bottom: 0; height: 56px;
    background: var(--band);
  }
  .front-band .display {
    position: absolute; right: 26px; top: 50%; transform: translateY(-50%);
    color: var(--orange); font-size: 22px;
  }
  .mascot-art {
    position: absolute; left: 10px; bottom: 0; width: 160px; height: 142px;
    border-radius: 10px 10px 0 0;
    background: linear-gradient(160deg, var(--art-red) 0%, var(--art-green) 30%, var(--art-skin) 62%, var(--art-blue) 100%);
  }
</style>
</head>
<body>

  <section class="card card--back" aria-label="Referral card, back">
    <div class="back-band"><span class="display">Keep me in your wallet and pass me on</span></div>
    <div class="details-heading">PLEASE FILL IN YOUR DETAILS</div>
    <div class="back-phone display">1300 574 862</div>
    <div class="referral-form">
      <div class="form-row"><span>Recommended by:</span><span class="fill"></span></div>
      <div class="form-row"><span>Address:</span><span class="fill"></span></div>
      <div class="form-row"><span>Friend's name:</span><span class="fill"></span></div>
    </div>
    <p class="fine-print">*this offer is only valued for work over $55. Non transferable for cash.<br>This coupon is limited to 1 per customer, not to be used in conjunction with any other offer</p>
    <div class="licence">Lic No: 381946D</div>
  </section>

  <section class="card card--front" aria-label="Referral card, front">
    <div class="offer-left">
      <div class="offer-big display">Two Free</div>
      <div class="offer-sub display">Movie tickets for referee</div>
    </div>
    <div class="ampersand">&amp;</div>
    <div class="offer-right">
      <div class="offer-big display">$25 Off</div>
      <div class="offer-sub display">On friend's first bill</div>
    </div>
    <div class="pitch">
      <div class="pitch-heading">HOW ABOUT TWO FREE MOVIE TICKETS?</div>
      <p>It is easy! Know someone who needs an electrician? Maybe a friend, family member, relative or work colleague. Tell them about us, and we will take $25 off their first bill and give you two FREE Movie Tickets just for introducing us. To make a referral fill out this card and give it to your friend.</p>
    </div>
    <div class="front-phone display">1300 574 862</div>
    <div class="front-band"><span class="display">Tell a friend for cash card</span></div>
    <div class="mascot-art" role="img" aria-label="Cartoon illustration of a masked hero mascot holding a light bulb"></div>
  </section>

</body>
</html>
```